TM Estates - Stone Hof Design

Looking for a double sides design, 1 side for my realestate and the other for home building. ( TM Estates on 1 side, Stone Hof card on the other Side
Side 1 - Priya Mond ~ Vex Realty logo and Company ( the Real estate district )
Priya Mond
Priya@Priyamondhomes.example
IG - Priya_Nwt_Agent
FB - priyam
Cell - 5550193847
3874 46 St Nw

Side 2
Priya Mond
5550193847
IG - Stonehof_Nwt
Stonehofbuild@mailbox.example

Target Market(s)

Home buyers/ sellers

Industry/Entity Type

Home builders - Realestate

Contact Information for Business Card

Above

Requirements
Must have
• Black OR White background - my information -

```html
<!DOCTYPE html>
<html lang="en">
<head>
<meta charset="UTF-8">
<title>TM Estates – Stone Hof Business Cards</title>
<link href="https://fonts.googleapis.com/css2?family=Tinos:wght@400;700&display=swap" rel="stylesheet">
<style>
  :root {
    --page-bg: #151518;
    --card-bg: #232328;
    --map-tone: #2c2c32;
    --edge-gold: #f6c531;
    --brand-blue: #1470c4;
    --brand-gold: #f6c531;
    --text-light: #f1f1f1;
    --rule: #b9b9bf;
  }
  * { box-sizing: border-box; margin: 0; padding: 0; }
  html, body { width: 1200px; height: 780px; overflow: hidden; }
  body {
    background: var(--page-bg);
    font-family: "Tinos", "Times New Roman", serif;
    position: relative;
  }
  .card {
    position: absolute;
    left: 280px;
    width: 640px;
    height: 360px;
    background: var(--card-bg);
    border-radius: 24px;
    border-bottom: 5px solid var(--edge-gold);
    border-right: 2px solid var(--edge-gold);
    overflow: hidden;
  }
  .card--builder { top: 18px; }
  .card--realty { top: 402px; }

  .card__map {
    position: absolute;
    left: 40px; top: 30px;
    width: 560px; height: 290px;
    border-radius: 120px;
    background: radial-gradient(ellipse at center, var(--map-tone) 0%, rgba(44,44,50,0.6) 55%, rgba(35,35,40,0) 75%);
  }
  .card__divider {
    position: absolute;
    left: 318px; top: 40px;
    width: 1px; height: 270px;
    background: linear-gradient(to bottom, rgba(185,185,191,0), var(--rule) 30%, var(--rule) 70%, rgba(185,185,191,0));
  }

  /* logo areas: kept within the left panel (0–300px) */
  .brand-mark {
    position: absolute;
    left: 40px;
    width: 260px;
    display: flex; align-items: center; gap: 12px;
    color: var(--brand-blue);
    font-weight: 700;
    white-space: nowrap;
  }
  .brand-mark__square {
    width: 16px; height: 16px;
    flex: none;
    background: var(--brand-gold);
  }
  .card--builder .brand-mark { top: 158px; font-size: 40px; letter-spacing: 1px; }
  .card--realty .brand-mark { top: 160px; font-size: 32px; letter-spacing: 2px; }

  .address {
    position: absolute;
    left: 356px; bottom: 36px;
    color: var(--text-light);
    font-size: 17px;
  }

  /* contact block */
  .contact {
    position: absolute;
    left: 350px; top: 56px;
    width: 270px;
    color: var(--text-light);
  }
  .card--realty .contact { top: 44px; }
  .contact__name { font-size: 32px; font-weight: 700; line-height: 1; }
  .contact__first { color: var(--brand-blue); }
  .contact__last { color: var(--brand-gold); }
  .contact__role { font-size: 15px; font-weight: 700; margin: 4px 0 16px 30px; }
  .contact__list { list-style: none; }
  .contact__item {
    display: flex; align-items: center; gap: 9px;
    font-size: 15px; line-height: 1; margin-bottom: 8px;
    white-space: nowrap;
  }
  .contact__icon { width: 14px; height: 14px; flex: none; }
  .contact__dot {
    width: 13px; height: 13px; flex: none;
    border-radius: 50%; border: 2px solid var(--brand-blue);
  }
  .contact__dot--solid { background: var(--brand-blue); }
</style>
</head>
<body>

<section class="card card--builder">
  <div class="card__map" role="img" aria-label="Faint dotted world map background"></div>
  <div class="brand-mark">
    <span class="brand-mark__square"></span>
    <span class="brand-mark__name">Stone Hof</span>
  </div>
  <div class="card__divider"></div>
  <div class="contact">
    <p class="contact__name"><span class="contact__first">Priya</span> <span class="contact__last">Mond</span></p>
    <p class="contact__role">Director</p>
    <ul class="contact__list">
      <li class="contact__item">
        <svg class="contact__icon" viewBox="0 0 24 24"><path fill="#1470c4" d="M6.6 10.8a15 15 0 0 0 6.6 6.6l2.2-2.2c.3-.3.7-.4 1-.2 1.1.4 2.3.6 3.6.6.6 0 1 .4 1 1V20c0 .6-.4 1-1 1A17 17 0 0 1 3 4c0-.6.4-1 1-1h3.5c.6 0 1 .4 1 1 0 1.3.2 2.5.6 3.6.1.3 0 .7-.2 1z"/></svg>
        5550193847
      </li>
      <li class="contact__item"><span class="contact__dot"></span>Stonehof_Nwt</li>
      <li class="contact__item">
        <svg class="contact__icon" viewBox="0 0 24 24"><rect x="2" y="5" width="20" height="14" fill="#1470c4"/><path d="M2 5l10 8 10-8" fill="none" stroke="#232328" stroke-width="2"/></svg>
        Stonehofbuild@mailbox.example
      </li>
    </ul>
  </div>
</section>

<section class="card card--realty">
  <div class="card__map" role="img" aria-label="Faint dotted world map background"></div>
  <div class="brand-mark">
    <span class="brand-mark__square"></span>
    <span class="brand-mark__name">PRIYA MOND</span>
  </div>
  <div class="card__divider"></div>
  <div class="contact">
    <p class="contact__name"><span class="contact__first">Priya</span> <span class="contact__last">Mond</span></p>
    <p class="contact__role">Director</p>
    <ul class="contact__list">
      <li class="contact__item">
        <svg class="contact__icon" viewBox="0 0 24 24"><path fill="#1470c4" d="M6.6 10.8a15 15 0 0 0 6.6 6.6l2.2-2.2c.3-.3.7-.4 1-.2 1.1.4 2.3.6 3.6.6.6 0 1 .4 1 1V20c0 .6-.4 1-1 1A17 17 0 0 1 3 4c0-.6.4-1 1-1h3.5c.6 0 1 .4 1 1 0 1.3.2 2.5.6 3.6.1.3 0 .7-.2 1z"/></svg>
        5550193847
      </li>
      <li class="contact__item"><span class="contact__dot contact__dot--solid"></span>priyam</li>
      <li class="contact__item"><span class="contact__dot"></span>Priya_Nwt_Agent</li>
      <li class="contact__item">
        <svg class="contact__icon" viewBox="0 0 24 24"><rect x="2" y="5" width="20" height="14" fill="#1470c4"/><path d="M2 5l10 8 10-8" fill="none" stroke="#232328" stroke-width="2"/></svg>
        Priya@Priyamondhomes.example
      </li>
      <li class="contact__item">
        <svg class="contact__icon" viewBox="0 0 24 24"><g fill="none" stroke="#1470c4" stroke-width="2"><circle cx="12" cy="12" r="10"/><ellipse cx="12" cy="12" rx="4" ry="10"/><path d="M2 12h20M4 7h16M4 17h16"/></g></svg>
        www.priyamondhomes.example
      </li>
    </ul>
  </div>
  <p class="address">3874 46 St Nw</p>
</section>

</body>
</html>
```